Simple infographic for paper attributes

Hello, we are a company that sells paper. Any kind of paper, envelopes, letter paper, handicraft paper etc.

We need a graphic / infographic which indicates to our customers that our paper / envelopes etc. are both printable with printers and writable with any pens.

Font styles to use
Serif
Sans Serif

Requirements
Must have
• - The format would be 3000x3000 pixels.
- The style would be simple and simple
Nice to have
• - The two terms "printable" and "writable" may be used

```html
<!DOCTYPE html>
<html lang="en">
<head>
<meta charset="utf-8">
<title>Our Paper – Printable &amp; Writable</title>
<link href="https://fonts.googleapis.com/css2?family=Poppins:wght@500&display=swap" rel="stylesheet">
<style>
  :root {
    --page: #ffffff;
    --panel: #f0f1f1;
    --ink: #2f2f2f;
    --blue: #29a9e1;
    --orange: #f7941d;
    --coral: #ff5f5f;
    --pencil: #e8322f;
    --shadow: #d9dbdb;
    --dash: #3a3a3a;
  }
  html, body {
    margin: 0;
    padding: 0;
    width: 1200px;
    height: 1200px;
    overflow: hidden;
    background: var(--page);
  }
  .canvas {
    position: relative;
    width: 1200px;
    height: 1200px;
  }
  .infographic {
    position: absolute;
    inset: 0;
  }
  .label {
    font-family: "Poppins", sans-serif;
    font-weight: 500;
    font-size: 38px;
    fill: #111;
  }
</style>
</head>
<body>
<main class="canvas">
  <svg class="infographic" width="1200" height="1200" viewBox="0 0 1200 1200" xmlns="http://www.w3.org/2000/svg">
    <defs>
      <linearGradient id="long-shadow" x1="0" y1="0" x2="1" y2="1">
        <stop offset="0" stop-color="var(--shadow)" stop-opacity="0.9"/>
        <stop offset="1" stop-color="var(--shadow)" stop-opacity="0"/>
      </linearGradient>
    </defs>

    <!-- background panel -->
    <rect class="panel" x="28" y="28" width="1144" height="1144" fill="var(--panel)"/>

    <!-- long shadows -->
    <g class="shadows">
      <polygon points="692,398 508,582 688,762 872,578" fill="url(#long-shadow)"/>
      <polygon points="400,643 266,777 420,931 554,797" fill="url(#long-shadow)"/>
      <polygon points="940,643 806,777 960,931 1094,797" fill="url(#long-shadow)"/>
    </g>

    <!-- connectors -->
    <g class="connectors" fill="none" stroke="var(--dash)" stroke-width="3" stroke-dasharray="10 6">
      <polyline points="445,490 333,490 333,615"/>
      <polyline points="770,490 876,490 876,615"/>
    </g>

    <!-- main node: paper -->
    <g class="node node--paper">
      <polygon points="443,490 482,462 482,518" fill="var(--blue)"/>
      <polygon points="772,490 733,462 733,518" fill="var(--blue)"/>
      <circle cx="604" cy="490" r="124" fill="var(--panel)" stroke="var(--blue)" stroke-width="13"/>
      <g class="icon" fill="var(--panel)" stroke="var(--ink)" stroke-width="6" stroke-linejoin="round">
        <rect x="573" y="434" width="84" height="120" rx="4"/>
        <path d="M566,410 H626 A4,4 0 0 1 630,414 V526 A4,4 0 0 1 626,530 H550 A4,4 0 0 1 546,526 V430 Z"/>
        <path d="M546,430 H566 V410" fill="none"/>
      </g>
    </g>

    <!-- printable node -->
    <g class="node node--printable">
      <circle cx="333" cy="710" r="92" fill="var(--panel)" stroke="var(--orange)" stroke-width="9"/>
      <g class="icon">
        <rect x="303" y="668" width="58" height="28" rx="3" fill="none" stroke="var(--ink)" stroke-width="5"/>
        <rect x="274" y="690" width="118" height="44" rx="8" fill="var(--ink)"/>
        <circle cx="380" cy="701" r="4" fill="var(--panel)"/>
        <rect x="300" y="712" width="64" height="40" rx="2" fill="var(--panel)" stroke="var(--ink)" stroke-width="5"/>
        <line x1="312" y1="727" x2="352" y2="727" stroke="var(--ink)" stroke-width="4"/>
        <line x1="312" y1="738" x2="352" y2="738" stroke="var(--ink)" stroke-width="4"/>
      </g>
    </g>

    <!-- writable node -->
    <g class="node node--writable">
      <circle cx="873" cy="710" r="92" fill="var(--panel)" stroke="var(--coral)" stroke-width="9"/>
      <g class="icon" stroke="var(--ink)" stroke-linecap="round" stroke-linejoin="round">
        <path d="M858,670 H898 A3,3 0 0 1 901,673 V752 A3,3 0 0 1 898,755 H845 A3,3 0 0 1 842,752 V686 Z" fill="var(--panel)" stroke-width="5"/>
        <path d="M842,686 H858 V670" fill="none" stroke-width="5"/>
        <line x1="856" y1="705" x2="884" y2="705" stroke-width="4"/>
        <line x1="856" y1="716" x2="888" y2="716" stroke-width="4"/>
        <line x1="856" y1="727" x2="888" y2="727" stroke-width="4"/>
        <line x1="856" y1="738" x2="884" y2="738" stroke-width="4"/>
      </g>
      <g class="pencil">
        <rect x="897" y="692" width="8" height="38" fill="var(--pencil)"/>
        <polygon points="897,730 905,730 901,740" fill="var(--ink)"/>
      </g>
    </g>

    <!-- labels -->
    <text class="label" x="600" y="312" text-anchor="middle">Our Paper</text>
    <text class="label" x="338" y="892" text-anchor="middle">Printable</text>
    <text class="label" x="891" y="892" text-anchor="middle">Writable</text>
  </svg>
</main>
</body>
</html>
```